Quarry Steelworks Capability Statement

Email template to promote our companies capabilities

Target Market(s)

Building companies
Architects

Requirements
Must have
• product list
• Our Products Include
• Boxes
• Brackets
• Boardwalk Frames
• Cable Ladder & Tray
• Cabinets
• Custom Pressings
• Decorative Cladding
• Decorative Panels
• Flashings
• Gates
• Louvered Panels
• Metal Roof Battens
• Metal Scaffold Planks
• Metal Art
• Purlins
• Perforated Metals
• Room Dividers
• Scaffold Planks
• Steel Angles
• Street Furniture
• Shelving & Storage Systems
• Stair Treads
• Stud Framing
• Tanks
• Tool Boxes
• Waste Bins
• Services
• Guillotining
• CNC Bending
• Punching
• Stamping
• Notching
• Cropping
• Coil Blanking
• Turret Punching
• Drilling and tapping
• Welding (MIG & TIG)

```html
<!DOCTYPE html>
<html lang="en">
<head>
<meta charset="utf-8">
<title>Quarry Steelworks Capability Statement</title>
<link rel="stylesheet" href="https://fonts.googleapis.com/css2?family=Lato:wght@300;400;700&display=swap">
<style>
:root{
  --red:#c4211f;
  --text:#333;
  --muted:#555;
  --panel:#f4f4f4;
  --white:#fff;
  --stage:#e9e9e9;
  --rule:#d4d4d4;
}
*{box-sizing:border-box;margin:0;padding:0}
html,body{width:900px;height:1200px;overflow:hidden;background:var(--stage);font-family:'Lato',sans-serif;color:var(--text)}
.email{position:absolute;left:264px;top:20px;width:600px;transform:scale(.62);transform-origin:top left;background:var(--panel);box-shadow:0 0 20px rgba(0,0,0,.25)}
.header{height:88px;background:var(--white);display:flex;justify-content:space-between;align-items:center;padding:0 14px 0 18px;border-bottom:1px solid var(--rule)}
.brand{display:flex;align-items:center;gap:10px}
.brand-mark{width:22px;height:22px;border-radius:50%;background:var(--red)}
.brand-name{font-size:24px;font-weight:400;color:var(--red);letter-spacing:.5px}
.contact-top{text-align:right}
.social{display:flex;justify-content:flex-end;gap:8px;margin-bottom:6px}
.social span{width:26px;height:26px;border-radius:50%;background:var(--red);display:block}
.call{font-size:19px;font-weight:300;color:#222}
.call b{font-weight:400}
.gallery{display:grid;grid-template-columns:198px 207px 187px;grid-template-rows:130px 130px;gap:3px;padding:3px 2px;background:var(--white)}
.photo{display:block}
.intro{background:var(--white);text-align:center;padding:40px 36px 28px}
.intro h1{color:var(--red);font-weight:400;font-size:25px;margin-bottom:16px}
.intro p{font-size:15px;font-weight:300;line-height:22px;color:var(--text)}
.intro .more{margin-top:8px}
.intro a{display:block;color:var(--red);font-size:19px;text-decoration:none;margin-top:4px}
.divider{height:2px;margin:0 60px;background:linear-gradient(90deg,transparent,#c8c8c8,transparent)}
.section{padding:38px 0 36px}
.plate{width:283px;height:38px;margin:0 auto 34px;background:linear-gradient(90deg,#9a9a9a,#e6e6e6 20%,#fafafa 45%,#bdbdbd 70%,#eee 85%,#999);display:flex;align-items:center;justify-content:space-between;padding:0 10px;color:var(--red);font-size:19px}
.plate .label{font-weight:400;flex:1;text-align:center}
.rivet{width:7px;height:7px;border-radius:50%;background:#777;box-shadow:inset 1px 1px 1px #eee}
.checklist{display:grid;grid-template-columns:300px 250px;padding-left:45px}
.checklist ul{list-style:none}
.checklist li{display:flex;align-items:center;gap:7px;font-size:17px;color:#333;height:28px}
.tick{width:16px;height:16px;flex:none}
.showcase{display:flex;justify-content:space-between;padding:50px 16px 50px 18px}
.showcase .photo{width:175px;height:170px;border:3px solid #333;border-radius:0 0 28px 0}
.contacts{display:flex;padding:40px 0 28px 36px;background:var(--panel)}
.person{font-size:14px;line-height:22px;color:#222;white-space:nowrap}
.person:first-child{width:244px}
.person + .person{border-left:1px solid var(--rule);padding-left:40px}
.person h3{color:var(--red);font-weight:400;font-size:19px;margin-bottom:2px}
.footer{height:42px;background:var(--red);color:var(--white);font-size:13px;font-weight:700;display:flex;align-items:center;justify-content:center}
</style>
</head>
<body>
<svg width="0" height="0" style="position:absolute">
  <symbol id="tick" viewBox="0 0 16 16">
    <rect x="1" y="3" width="12" height="12" rx="2" fill="none" stroke="#c4211f" stroke-width="2"/>
    <path d="M4 8.5l3 3L15 2" fill="none" stroke="#c4211f" stroke-width="2.6" stroke-linecap="round"/>
  </symbol>
</svg>
<main class="email">
  <header class="header">
    <div class="brand"><span class="brand-mark"></span><span class="brand-name">QUARRY STEELWORKS</span></div>
    <div class="contact-top">
      <div class="social"><span></span><span></span><span></span></div>
      <div class="call">Call Us: <b>08 5550 4120</b></div>
    </div>
  </header>
  <section class="gallery">
    <div class="photo" role="img" aria-label="Steel roof frame under construction" style="background:linear-gradient(#cfd8e0,#8c98a4)"></div>
    <div class="photo" role="img" aria-label="Stacked galvanised steel sections" style="background:linear-gradient(#d8dadc,#9aa0a4)"></div>
    <div class="photo" role="img" aria-label="Stacked corrugated steel profiles" style="background:linear-gradient(#eceff1,#8d9399)"></div>
    <div class="photo" role="img" aria-label="Modern house with steel balcony" style="background:linear-gradient(#c9d3dc,#a6a8a8)"></div>
    <div class="photo" role="img" aria-label="Fabrication workshop floor" style="background:linear-gradient(#b9b4a8,#6f6b63)"></div>
    <div class="photo" role="img" aria-label="Ceiling stud framing grid" style="background:linear-gradient(#bfc3c8,#7a7f86)"></div>
  </section>
  <section class="intro">
    <h1>Quarry Steelworks.... Steel Shaped Simply!</h1>
    <p>Established in 1981, we manufacture quality steel components to the building, mining and electrical industries. Offering friendly and personalised service for all your steel needs, we can customise our products dependant on our customer needs.</p>
    <p class="more">For more information Visit:</p>
    <a href="#">www.quarrysteelworks.com.au</a>
  </section>
  <div class="divider"></div>
  <section class="section">
    <div class="plate"><span class="rivet"></span><span class="label">OUR PRODUCTS INCLUDE</span><span class="rivet"></span></div>
    <div class="checklist">
      <ul>
        <li><svg class="tick"><use href="#tick"/></svg>Boxes</li>
        <li><svg class="tick"><use href="#tick"/></svg>Brackets</li>
        <li><svg class="tick"><use href="#tick"/></svg>Boardwalk Frames</li>
        <li><svg class="tick"><use href="#tick"/></svg>Cable Ladder &amp; Tray</li>
        <li><svg class="tick"><use href="#tick"/></svg>Cabinets</li>
        <li><svg class="tick"><use href="#tick"/></svg>Custom Pressings</li>
        <li><svg class="tick"><use href="#tick"/></svg>Decorative Cladding</li>
        <li><svg class="tick"><use href="#tick"/></svg>Decorative Panels</li>
        <li><svg class="tick"><use href="#tick"/></svg>Flashings</li>
        <li><svg class="tick"><use href="#tick"/></svg>Gates</li>
        <li><svg class="tick"><use href="#tick"/></svg>Louvered Panels</li>
        <li><svg class="tick"><use href="#tick"/></svg>Metal Roof Battens</li>
        <li><svg class="tick"><use href="#tick"/></svg>Metal Scaffold Planks</li>
      </ul>
      <ul>
        <li><svg class="tick"><use href="#tick"/></svg>Metal Art</li>
        <li><svg class="tick"><use href="#tick"/></svg>Purlins</li>
        <li><svg class="tick"><use href="#tick"/></svg>Perforated Metals</li>
        <li><svg class="tick"><use href="#tick"/></svg>Room Dividers</li>
        <li><svg class="tick"><use href="#tick"/></svg>Scaffold Planks</li>
        <li><svg class="tick"><use href="#tick"/></svg>Steel Angles</li>
        <li><svg class="tick"><use href="#tick"/></svg>Street Furniture</li>
        <li><svg class="tick"><use href="#tick"/></svg>Shelving &amp; Storage Systems</li>
        <li><svg class="tick"><use href="#tick"/></svg>Stair Treads</li>
        <li><svg class="tick"><use href="#tick"/></svg>Stud Framing</li>
        <li><svg class="tick"><use href="#tick"/></svg>Tanks</li>
        <li><svg class="tick"><use href="#tick"/></svg>Tool Boxes</li>
        <li><svg class="tick"><use href="#tick"/></svg>Waste Bins</li>
      </ul>
    </div>
  </section>
  <div class="divider"></div>
  <section class="section" style="padding-bottom:0">
    <div class="plate"><span class="rivet"></span><span class="label">SERVICES</span><span class="rivet"></span></div>
    <div class="checklist">
      <ul>
        <li><svg class="tick"><use href="#tick"/></svg>Guillotining</li>
        <li><svg class="tick"><use href="#tick"/></svg>CNC Bending</li>
        <li><svg class="tick"><use href="#tick"/></svg>Punching</li>
        <li><svg class="tick"><use href="#tick"/></svg>Stamping</li>
        <li><svg class="tick"><use href="#tick"/></svg>Notching</li>
      </ul>
      <ul>
        <li><svg class="tick"><use href="#tick"/></svg>Cropping</li>
        <li><svg class="tick"><use href="#tick"/></svg>Coil Blanking</li>
        <li><svg class="tick"><use href="#tick"/></svg>Turret Punching</li>
        <li><svg class="tick"><use href="#tick"/></svg>Drilling and tapping</li>
        <li><svg class="tick"><use href="#tick"/></svg>Welding (MIG &amp; TIG)</li>
      </ul>
    </div>
    <div class="showcase">
      <div class="photo" role="img" aria-label="Restaurant shopfront with decorative metal screens" style="background:linear-gradient(#8a3a26,#6b6b6b 55%,#9a9a96)"></div>
      <div class="photo" role="img" aria-label="Press brake machine in the workshop" style="background:linear-gradient(#7d8389,#c9432f 50%,#585b5e)"></div>
      <div class="photo" role="img" aria-label="House facade with laser-cut screen panels" style="background:linear-gradient(#3b6bb5,#bfc0bd 50%,#5e5149)"></div>
    </div>
  </section>
  <div class="divider"></div>
  <section class="contacts">
    <div class="person">
      <h3>Dana Holloway</h3>
      State Manager<br>Call: 08 5550 3106<br>d.holloway@quarrysteelworks.com.au
    </div>
    <div class="person">
      <h3>Marcus Reid</h3>
      Sales Manager<br>Call: 08 5550 3139<br>marcus.reid@quarrysteelworks.com.au
    </div>
  </section>
  <footer class="footer">Copyright @ 2019 quarrysteelworks</footer>
</main>
</body>
</html>
```